Business Card for Consulting Company

I would need a business card for my consulting company - the company brand and logos are defined and shared as part of this project. The proposed design for the business card can be reused as inspiration for my email signature.

```html
<!DOCTYPE html>
<html lang="en">
<head>
<meta charset="utf-8">
<title>Halvern Partners – Business Card</title>
<link href="https://fonts.googleapis.com/css2?family=Montserrat:wght@500;600&family=Roboto:wght@400&display=swap" rel="stylesheet">
<style>
  :root {
    --page-bg: #ffffff;
    --card-front: #e6e6e6;
    --card-back: #02a9ab;
    --teal: #0fa8a8;
    --teal-light: rgba(0, 226, 226, 0.6);
    --teal-dark: rgba(4, 104, 106, 0.6);
    --teal-clear: rgba(2, 169, 171, 0);
    --ink: #3d3d3d;
    --white: #ffffff;
  }
  * { margin: 0; padding: 0; box-sizing: border-box; }
  html, body {
    width: 1093px; height: 1200px; overflow: hidden;
    background: var(--page-bg);
  }
  .sheet { position: relative; width: 1093px; height: 1200px; }

  .card {
    position: absolute;
    left: 265px;
    width: 580px;
    height: 357px;
    overflow: hidden;
  }
  .card--front { top: 226px; background: var(--card-front); text-align: center; }
  .card--back { top: 620px; background: var(--card-back); }

  /* Front */
  .brand {
    position: absolute; left: 0; right: 0; top: 72px;
    display: flex; align-items: center; justify-content: center; gap: 10px;
    font-family: "Montserrat", sans-serif; font-weight: 600;
    font-size: 26px; letter-spacing: 0.3px; color: var(--teal);
    line-height: 32px;
  }
  .brand__dot { width: 18px; height: 18px; border-radius: 50%; background: var(--teal); flex: none; }

  .person {
    position: absolute; left: 0; right: 0; top: 185px;
    font-family: "Montserrat", sans-serif; font-weight: 500;
    font-size: 20px; line-height: 26px; letter-spacing: 1.8px; color: var(--ink);
  }
  .person__surname { color: var(--teal); }
  .role {
    position: absolute; left: 0; right: 0; top: 213px;
    font-family: "Roboto", sans-serif; font-size: 13.5px; line-height: 18px;
    letter-spacing: 1.6px; color: var(--ink);
  }
  .divider {
    position: absolute; top: 240px; left: 253px; width: 74px; height: 1px;
    background: var(--teal);
  }
  .contact {
    position: absolute; left: 0; right: 0; top: 252px;
    list-style: none;
    font-family: "Roboto", sans-serif; color: var(--ink);
    letter-spacing: 1.4px;
  }
  .contact__phone { font-size: 16px; line-height: 22px; }
  .contact__line { font-size: 13.5px; line-height: 22px; }

  /* Back */
  .emblem-area {
    position: absolute; left: 0; top: 0; width: 340px; height: 100%;
    background: linear-gradient(180deg, var(--teal-light) 0%, var(--teal-clear) 48%, var(--teal-clear) 58%, var(--teal-dark) 100%);
  }
  .brand--back {
    position: absolute; left: 322px; top: 170px;
    display: flex; align-items: center; gap: 10px;
    font-family: "Montserrat", sans-serif; font-weight: 600;
    font-size: 21px; line-height: 28px; letter-spacing: 0.3px; color: var(--white);
    white-space: nowrap;
  }
  .brand--back .brand__dot { background: var(--white); width: 15px; height: 15px; }
</style>
</head>
<body>
<main class="sheet">
  <section class="card card--front" aria-label="Business card front">
    <div class="brand"><span class="brand__dot"></span><span class="brand__name">Halvern Partners</span></div>
    <h1 class="person">MARCEL <span class="person__surname">AUBRY</span></h1>
    <p class="role">FOUNDER &amp; CEO</p>
    <div class="divider"></div>
    <ul class="contact">
      <li class="contact__phone">044-555 010 203</li>
      <li class="contact__line">INFO@HALVERNPARTNERS.COM</li>
      <li class="contact__line">WWW.HALVERNPARTNERS.COM</li>
    </ul>
  </section>

  <section class="card card--back" aria-label="Business card back">
    <div class="emblem-area" role="img" aria-label="Large embossed brand emblem in light and dark teal"></div>
    <div class="brand--back"><span class="brand__dot"></span><span class="brand__name">Halvern Partners</span></div>
  </section>
</main>
</body>
</html>
```